NEW Gummy line needs fabulous, eye catching, juicy packaging!

***PLEASE NOTE: this is ONE bag, with THREE FLAVORS in the one bag. We are looking for a design that visually represents the three flavors in the bag*****

We are a well established cannabis company in Washington State, looking to launch a new line of gummies that are more affordable for the marketplace as people struggle with rising prices. The new brand name is "Thistle & Company" and the product will be called "Meadow Bramble" - every bag is a MULTI-FLAVOR pack of 3 flavors (Washington State Cherry, Blue Elderberry, Royal Purple Raspberry) and an example of the gummy berry shape has been uploaded. We are looking for the packaging to reflect the three fruit flavors inside the bag - and can also have images of the shape of the gummies inside - I will upload an example of the gummy shape for reference also.

There are a number of "required elements" for state compliance in our state, so I will upload an example of our current 'PAVLA' brand APPLE flavor packaging so you can see how those "required elements" appear (Not for Kids icon, 21+ icon, the weight, the serving size information, 100mg THC/bag, and all the warning language is the same for this product as the APPLE example bag I have uploaded). Please reference the APPLE packaging for the icons and copy ONLY - this contest is for Thistle & Company which is a new brand and we would like to see completely new concepts as both brands will be sold in the same stores.

We are most concerned with the visual concept - so no need to get all the placements, or all of the required elements for this initial contest, we can work together to perfect it once chosen. But in past competitions, designers have found it helpful to know for placement.

***NO CANNABIS IMAGERY PLEASE***

The products are sold in specialty dispensaries so customers are aware the products contain THC. We are more so looking for retail packaging that is trendy, modern, eye catching and enticing for a gummy food product.

**I have also uploaded a "KERPLINKS" package and a "TOVA" - they are competitors - so we don't want to look like them, but providing it for inspiration where they mix the candy and the fruit, which can also be an idea for us.

PLEASE NOTE: This is a one bag design - each bag contains three flavors. So the design should reflect an mix of the 3 berry flavors

I am extending the deadline as we were able to push our print deadline back and I would like to give designers the weekend for their submissions. I also clarified the brief - ONE BAG, 3 FLAVORS inside - and hoping this is helpful for the designers also.

Target Market(s)

21+ THC Gummy lovers in Washington state

Industry/Entity Type

Cannabis Edibles

Requirements
Must have
• BOLD, eye catching, delicious design that is appealing for a gummy product (berries and product image a PLUS)
Nice to have
• incorporate the berries as visual, orchard visuals, organic but vibrant and juicy and fun
Should not have
• NO CANNABIS IMAGERY PLS

```html
<!DOCTYPE html>
<html lang="en">
<head>
<meta charset="utf-8">
<title>Meadow Bramble – Thistle &amp; Company</title>
<link rel="stylesheet" href="https://fonts.googleapis.com/css2?family=Zilla+Slab:wght@400;500;700&family=Barlow+Condensed:wght@600;700&display=swap">
<style>
  :root {
    --stage: #dcdcdc;
    --bag: #000000;
    --white: #ffffff;
    --cherry: #ee2a33;
    --elder: #00aeef;
    --raspberry: #93278f;
    --warn-yellow: #f3ea3a;
    --warn-red: #c8202a;
  }
  * { box-sizing: border-box; margin: 0; padding: 0; }
  html, body { width: 1200px; height: 1055px; overflow: hidden; }
  body { background: var(--stage); position: relative; font-family: "Zilla Slab", Georgia, serif; }

  .bag {
    position: absolute; left: 321px; top: 119px; width: 544px; height: 844px;
    background: var(--bag); border-radius: 14px; overflow: hidden;
  }

  .swirl {
    position: absolute; left: 0; top: 90px; width: 544px; height: 640px;
    background:
      radial-gradient(ellipse 38% 36% at 52% 52%, var(--bag) 0 55%, transparent 75%),
      radial-gradient(ellipse 60% 55% at 50% 50%, rgba(147,39,143,.85) 0 40%, transparent 70%),
      conic-gradient(from 20deg at 50% 50%, var(--cherry), var(--elder), var(--raspberry), var(--cherry), var(--elder), var(--raspberry), var(--cherry));
    border-radius: 50% 50% 45% 45%;
    opacity: .92;
  }

  .age-badge {
    position: absolute; left: 55px; top: 30px; width: 50px; height: 50px;
    background: var(--warn-yellow); border: 3px solid var(--white);
    transform: rotate(45deg);
  }
  .child-warning {
    position: absolute; left: 129px; top: 26px; width: 40px; height: 40px;
    background: var(--warn-red);
  }
  .emergency {
    position: absolute; left: 129px; top: 72px; color: var(--warn-red);
    font: 600 8px/1.2 "Barlow Condensed", Arial, sans-serif; letter-spacing: .4px;
  }

  .product-name {
    position: absolute; left: 0; width: 544px; text-align: center; color: var(--white);
    font-weight: 700; line-height: 1;
    -webkit-text-stroke: 12px var(--bag); paint-order: stroke fill;
  }
  .product-name.line-1 { top: 148px; font-size: 78px; letter-spacing: 1px; }
  .product-name.line-2 { top: 228px; font-size: 62px; }

  .arch {
    position: absolute; left: 141px; top: 304px; width: 275px; height: 600px;
    background: var(--bag); border: 5px solid var(--white); border-bottom: none;
    border-radius: 138px 138px 0 0;
  }

  .brand {
    position: absolute; left: 141px; top: 368px; width: 275px; text-align: center;
    color: var(--white); font-weight: 500; font-size: 40px; line-height: 1.05;
  }

  .flavor-icon { position: absolute; left: 189px; width: 30px; height: 26px; border-radius: 50%; }
  .flavor-icon.cherry { top: 502px; background: var(--cherry); }
  .flavor-icon.elder { top: 535px; background: var(--elder); }
  .flavor-icon.raspberry { top: 567px; background: var(--raspberry); }

  .flavor {
    position: absolute; left: 230px; right: 0; height: 21px; padding-left: 16px;
    color: var(--white); font-size: 19px; font-weight: 500; line-height: 21px;
    clip-path: polygon(10px 0, 100% 0, 100% 100%, 10px 100%, 0 50%);
    white-space: nowrap;
  }
  .flavor.cherry { top: 505px; background: var(--cherry); }
  .flavor.elder { top: 538px; background: var(--elder); }
  .flavor.raspberry { top: 570px; background: var(--raspberry); }

  .pill {
    position: absolute; height: 23px; background: var(--white); color: var(--elder);
    font-size: 15px; font-weight: 500; line-height: 23px; text-align: center;
    clip-path: polygon(9px 0, calc(100% - 9px) 0, 100% 50%, calc(100% - 9px) 100%, 9px 100%, 0 50%);
  }
  .pill.dose { left: 231px; top: 609px; width: 104px; }
  .pill.strain { left: 423px; top: 729px; width: 74px; }

  .gummies {
    position: absolute; left: 171px; top: 646px; width: 223px; height: 147px;
    background: radial-gradient(circle at 60% 28%, var(--cherry) 0 20%, transparent 34%),
                radial-gradient(circle at 25% 45%, #8a1f5f 0 18%, transparent 30%),
                radial-gradient(circle at 20% 78%, var(--raspberry) 0 18%, transparent 30%),
                radial-gradient(circle at 82% 78%, var(--elder) 0 16%, transparent 28%),
                radial-gradient(circle at 52% 72%, #f4553e 0 18%, transparent 30%);
  }

  .count { position: absolute; left: 423px; top: 758px; color: var(--elder); font-size: 36px; line-height: 1; }
  .count-label { position: absolute; left: 467px; top: 766px; font-size: 12px; line-height: 1.2; color: var(--white); }
  .count-label .accent { color: var(--elder); }

  .net-weight {
    position: absolute; left: 141px; top: 806px; width: 275px; text-align: center;
    color: var(--white); font-size: 16px;
  }
</style>
</head>
<body>
  <main class="bag">
    <div class="swirl" role="img" aria-label="Swirling red, blue and purple berry-juice pattern"></div>

    <div class="age-badge" role="img" aria-label="Age restriction badge"></div>
    <div class="child-warning" role="img" aria-label="Child safety warning badge"></div>
    <p class="emergency">EMERGENCY<br>(800) 555 0142</p>

    <h1>
      <span class="product-name line-1">MEADOW</span>
      <span class="product-name line-2">BRAMBLE</span>
    </h1>

    <div class="arch"></div>
    <p class="brand">Thistle<br>&amp; Company</p>

    <div class="flavor-icon cherry" role="img" aria-label="Cherry icon"></div>
    <div class="flavor-icon elder" role="img" aria-label="Elderberry icon"></div>
    <div class="flavor-icon raspberry" role="img" aria-label="Raspberry icon"></div>
    <p class="flavor cherry">WASHINGTON STATE CHERRY</p>
    <p class="flavor elder">BLUE ELDERBERRY</p>
    <p class="flavor raspberry">ROYAL PURPLE RASPBERRY</p>

    <p class="pill dose">100MG THC</p>
    <div class="gummies" role="img" aria-label="Photo of berry-shaped gummies in purple, red, orange and blue"></div>

    <p class="pill strain">INDICA</p>
    <p class="count">10</p>
    <p class="count-label"><span class="accent">PIECES</span><br>PER BAG</p>

    <p class="net-weight">NET WT 2.2 OZ (62G)</p>
  </main>
</body>
</html>
```